Brochure design for 3D ultrasound company

I am looking for a clean and modern and edgy brochure for my ultrasound company. We are a fairly new company specialize in 3D/4D ultrasounds.Our brochures will be placed in OB-GYN offices in high end areas around Los Angeles, so we need something that will stand out and capture a modern woman's attention. Our logo is currently in the process of being designed, so I don't have a picture to provide quite yet, however it will be our company name"Kite + Fern" written in a special font that looks like neon lights. I will attach a few images of what our logo will be like, and some initial content that can help provide the layout we would like for the brochure. please feel free to also take a look at our website. www.kitefernscans.example.

Target Market(s)

Upscale trendy women.

Colors
eea4c8
33a6d7
fee18a

Requirements
Should not have
• too many colors.

```html
<!DOCTYPE html>
<html lang="en">
<head>
<meta charset="utf-8">
<title>Kite + Fern — Tri-fold Brochure, Outside</title>
<link rel="stylesheet" href="https://fonts.googleapis.com/css2?family=Oswald:wght@500;600&family=Montserrat:wght@400;500;600&display=swap">
<style>
  :root {
    --pink: #f05a9a;
    --pink-soft: #eea4c8;
    --pink-title: #f27db5;
    --coral: #f26a4f;
    --orange: #f7934a;
    --yellow: #fee18a;
    --peach: #f6c6a8;
    --ink: #2d2d2d;
    --paper: #ffffff;
    --mist: #ececec;
    --backdrop: #f4eef1;
  }
  * { box-sizing: border-box; margin: 0; padding: 0; }
  html, body { width: 1200px; height: 800px; overflow: hidden; background: var(--backdrop); }
  .brochure {
    position: absolute; left: 0; top: 0; width: 1200px; height: 800px;
    display: grid; grid-template-columns: repeat(3, 400px);
    background: var(--paper);
    font-family: "Montserrat", sans-serif; color: var(--ink);
  }
  .panel { position: relative; overflow: hidden; border-right: 1px solid #f1f1f1; }
  .panel:last-child { border-right: none; }
  .deco { position: absolute; left: 0; top: 0; width: 400px; height: 800px; pointer-events: none; }

  /* Panel 1: What's what */
  .whats-what { position: absolute; left: 50px; top: 52px; width: 270px; z-index: 2; }
  .whats-what h2 {
    font-family: "Oswald", sans-serif; font-weight: 600; font-style: italic;
    font-size: 26px; letter-spacing: 0.5px; color: var(--ink); margin-bottom: 12px;
  }
  .term { font-size: 11px; line-height: 1.45; margin-bottom: 9px; }
  .term b { color: var(--pink); font-weight: 600; margin-right: 3px; }
  .side-tab { position: absolute; left: 0; top: 250px; width: 22px; height: 44px; background: var(--pink); }
  .photo-friends {
    position: absolute; left: 0; top: 430px; width: 400px; height: 370px;
    background: linear-gradient(160deg, #f7cbb2 0%, #f1a7b7 45%, #a9c7dd 100%);
  }

  /* Panel 2: About and contact */
  .photo-belly {
    position: absolute; left: 40px; top: 36px; width: 320px; height: 230px;
    background: linear-gradient(135deg, #f4f1ee 0%, #e9c39f 55%, #5a4d48 100%);
  }
  .about { position: absolute; left: 40px; top: 300px; width: 320px; font-size: 12px; line-height: 1.55; text-align: center; }
  .call-now { position: absolute; left: 58px; top: 460px; display: flex; align-items: center; gap: 12px; }
  .call-now .label { font-family: "Oswald", sans-serif; font-weight: 600; font-style: italic; font-size: 20px; line-height: 1; }
  .call-now .number { font-family: "Oswald", sans-serif; font-weight: 500; font-style: italic; font-size: 30px; color: var(--pink-title); line-height: 1.1; }
  .contacts { position: absolute; left: 58px; top: 555px; list-style: none; font-size: 12px; font-weight: 600; line-height: 1.9; }
  .contacts li { display: flex; align-items: center; gap: 10px; }
  .contacts .dot { width: 8px; height: 8px; border-radius: 50%; background: var(--ink); }

  /* Panel 3: Cover */
  .photo-cover {
    position: absolute; left: 57px; top: 95px; width: 286px; height: 286px; border-radius: 50%;
    background: linear-gradient(180deg, #e8e4e0 0%, #2e3f6b 38%, #f2efec 62%, #e6dcd4 100%);
  }
  .brand { position: absolute; left: 0; top: 420px; width: 400px; text-align: center; }
  .brand .name { font-family: "Montserrat", sans-serif; font-weight: 500; font-size: 32px; color: var(--pink); letter-spacing: 1px; }
  .brand .tag { font-size: 11px; color: var(--pink); letter-spacing: 1px; }
  .headline { position: absolute; left: 38px; top: 500px; width: 340px; }
  .headline h1 {
    font-family: "Oswald", sans-serif; font-weight: 600; font-style: italic;
    font-size: 50px; line-height: 1; color: var(--pink-title); letter-spacing: -0.5px;
  }
  .headline .sub { font-family: "Oswald", sans-serif; font-weight: 600; font-style: italic; font-size: 18px; line-height: 1.2; color: var(--ink); margin-top: 4px; }
  .headline .sub-pink { font-family: "Oswald", sans-serif; font-weight: 500; font-style: italic; font-size: 18px; line-height: 1.2; color: var(--pink-title); }
  .call-today { position: absolute; left: 100px; top: 655px; display: flex; align-items: center; gap: 12px; }
  .call-today .label { font-family: "Oswald", sans-serif; font-weight: 600; font-style: italic; font-size: 20px; line-height: 1; }
  .call-today .number { font-family: "Oswald", sans-serif; font-weight: 500; font-style: italic; font-size: 30px; color: var(--pink-title); line-height: 1.1; }
  .website { position: absolute; left: 0; bottom: 26px; width: 400px; text-align: center; font-size: 13px; font-weight: 600; letter-spacing: 3px; }
  .website .www, .website .com { color: var(--pink); }
</style>
</head>
<body>
<main class="brochure">

  <section class="panel panel-explainer">
    <svg class="deco" viewBox="0 0 400 800" aria-hidden="true">
      <path d="M230 0 C300 40 360 120 400 190 L400 0 Z" fill="var(--pink-soft)"/>
      <path d="M250 0 C310 30 370 80 400 120 L400 0 Z" fill="var(--pink)" opacity="0.85"/>
    </svg>
    <div class="side-tab"></div>
    <div class="whats-what">
      <h2>WHAT'S WHAT...</h2>
      <p class="term"><b>2D</b>is the traditional black and white photo—you know, the one that you want to get emotional about, but you don't know what you're looking at.</p>
      <p class="term"><b>3D</b>is an image of the fetus and it's features. So you can see the baby has dad's nose, and mom's lips.</p>
      <p class="term"><b>4D</b>is 3D, but with motion. You can see the baby yawn, move it's arm, or even give you a smile.</p>
      <p class="term"><b>HD</b>is also 3D, but better. Now you can see a rendering of the baby's skin making it the most realistic fetal image possible. We are one of the few in Los Angeles that have the newest HD capable machines.</p>
    </div>
    <div class="photo-friends" role="img" aria-label="Photo of two expectant mothers in crop tops and jeans showing their bumps"></div>
    <svg class="deco" viewBox="0 0 400 800" aria-hidden="true">
      <path d="M0 430 L0 410 C110 390 210 400 260 430 C180 415 80 418 0 430 Z" fill="var(--pink-soft)"/>
      <path d="M400 580 C410 690 360 765 290 800 L400 800 Z" fill="var(--paper)"/>
      <path d="M380 580 C400 680 360 765 290 800 L310 800 C370 755 395 670 380 580 Z" fill="var(--yellow)"/>
    </svg>
  </section>

  <section class="panel panel-about">
    <div class="photo-belly" role="img" aria-label="Photo of hands holding an ultrasound print against a pregnant belly"></div>
    <p class="about">Kite + Fern is a mobile 3D ultrasound company servicing Los Angeles and surrounding areas. We take great pride in being one of LA's first mobile Ultrasound companies and for being an all female business! Our mission is to provide an unforgettable experience for expectant mothers in the comfort of their home!</p>
    <div class="call-now">
      <svg width="30" height="42" viewBox="0 0 30 42" aria-hidden="true"><path d="M22 2 C10 4 4 14 4 21 C4 28 10 38 22 40 L26 32 C18 31 14 26 14 21 C14 16 18 11 26 10 Z" fill="var(--ink)"/></svg>
      <div><div class="label">CALL US NOW</div><div class="number">(310) 555-0147</div></div>
    </div>
    <ul class="contacts">
      <li><span class="dot"></span>@kitefernscans</li>
      <li><span class="dot"></span>Kite_fern</li>
      <li><span class="dot"></span>www.kitefernscans.example</li>
      <li><span class="dot"></span>Email: info@kitefernscans.example</li>
    </ul>
  </section>

  <section class="panel panel-cover">
    <svg class="deco" viewBox="0 0 400 800" aria-hidden="true">
      <path d="M0 0 L400 0 L400 110 C300 50 150 30 0 60 Z" fill="var(--orange)"/>
      <path d="M120 0 L400 0 L400 110 C330 60 230 20 120 0 Z" fill="var(--coral)" opacity="0.8"/>
      <path d="M200 40 C300 50 370 80 400 110 L400 40 Z" fill="var(--pink)" opacity="0.7"/>
      <circle cx="200" cy="238" r="152" fill="none" stroke="var(--pink-soft)" stroke-width="6"/>
      <path d="M345 200 A152 152 0 0 1 120 368" fill="none" stroke="var(--yellow)" stroke-width="10"/>
      <path d="M0 720 C60 690 90 740 130 800 L0 800 Z M260 800 C300 740 340 700 400 720 L400 800 Z" fill="var(--mist)"/>
    </svg>
    <div class="photo-cover" role="img" aria-label="Photo of an expectant mother on a bed holding up an ultrasound strip"></div>
    <div class="brand">
      <div class="name">Kite + Fern</div>
      <div class="tag">3D ultrasound</div>
    </div>
    <div class="headline">
      <h1>KITE + FERN</h1>
      <p class="sub">A MOBILE 3D/4D ULTRASOUND SERVICE</p>
      <p class="sub-pink">ULTRASOUND IN THE COMFORT OF YOUR HOME.</p>
    </div>
    <div class="call-today">
      <svg width="30" height="42" viewBox="0 0 30 42" aria-hidden="true"><path d="M22 2 C10 4 4 14 4 21 C4 28 10 38 22 40 L26 32 C18 31 14 26 14 21 C14 16 18 11 26 10 Z" fill="var(--ink)"/></svg>
      <div><div class="label">CALL TODAY!</div><div class="number">(310) 555-0147</div></div>
    </div>
    <p class="website"><span class="www">WWW.</span>KITEFERNSCANS<span class="com">.EXAMPLE</span></p>
  </section>

</main>
</body>
</html>
```